Flyer Design for Non-Profit working with people with mental disabilities

We are Harbor Pathways, a non profit working with people with disabilities and helping them to live the best life they can.

We need a modern pamphlet designed for our service offerings. We don't want a single completed pamphlet, but 2 templates which we can then add our own photos and text to. We need:
*One double sided 210mm x 100mm template in portrait orientation
*One double sided 210mm x 200mm folded template in portrait orientation

The pamphlets need to be bold, happy, concise and easy to understand.

As for the content which we will add later we need room on both the front and back of the flier to add photos and text in later similar to the 5 Lanterns pamphlet.

As for the other flyer designs I uploaded, I like their simple, bold designs.

Also I uploaded a Harbor Works logo as well. I would like the logos to be switched out for a second copy of the templates with the different logo.
Updates

So just so everyone's on the same page here. I want to use this as a template for multiple separate services. I want a section on the front page for a pictures which I can change to suit the service, room for a clear title, and a paragraph of text. Refer to the 5 lanterns example to get an idea of what I'm looking for. On the back I was room for text. Don't worry about the photos I uploaded, I don't actually want photos with alpha backgrounds on the flyer, they were for one of the designers to use but I didn't like it. Just use stock photos of happy people for now. Again refer to the 5 lanterns example of how they're photos were set out. Thanks.

Target Market(s)

The families and carers of people with disabilities

Industry/Entity Type

Non Profit

Font styles to use
Other font styles liked:
• Museo Sans 300 and Museo Sans 500

Requirements
Must have
• The Harbor Pathways logo
• And our tagline: We listen, We plan, We do, We care
Nice to have
• A colour scheme which ties in well with our logo

```html
<!DOCTYPE html>
<html lang="en">
<head>
<meta charset="utf-8">
<title>Harbor Pathways – Children &amp; Families</title>
<link rel="stylesheet" href="https://fonts.googleapis.com/css2?family=Bebas+Neue&family=Mulish:wght@400;600&family=Oswald:wght@500;600&display=swap">
<style>
  :root {
    --purple-deep: #4e1f8c;
    --purple: #6a2497;
    --magenta: #b8268f;
    --heading: #8a2b9c;
    --accent-pink: #e243a6;
    --text: #333338;
    --white: #ffffff;
    --skin: #e2b49c;
    --hair-dark: #4a3a34;
    --vest: #e8692a;
    --jacket: #2b2a30;
    --studio-light: #d9d4d2;
    --studio-grey: #8f8b8c;
    --jersey: #7fa8cc;
    --sky: #9ec6e4;
    --sea: #5f93b8;
    --grass: #8fa36a;
  }
  * { margin: 0; padding: 0; box-sizing: border-box; }
  html, body { width: 1200px; height: 2520px; overflow: hidden; background: var(--white); }
  .flyer { position: relative; width: 1200px; height: 2520px; overflow: hidden; background: var(--white); }
  .bands { position: absolute; inset: 0; }

  .brand {
    position: absolute; top: 150px; left: 0; width: 1200px;
    display: flex; align-items: center; justify-content: center; gap: 34px;
  }
  .brand-dot { width: 70px; height: 70px; border-radius: 50%; background: var(--white); }
  .brand-name {
    font-family: "Oswald", sans-serif; font-weight: 600; color: var(--white);
    font-size: 96px; line-height: 1; letter-spacing: 2px; text-transform: uppercase;
  }

  .photo { position: absolute; overflow: hidden; box-shadow: inset 0 0 60px rgba(0,0,0,0.18); }
  .photo-portrait-left {
    left: 0; top: 472px; width: 505px; height: 583px;
    background:
      radial-gradient(ellipse 34% 30% at 50% 38%, var(--skin) 0%, rgba(226,180,156,0.6) 55%, rgba(226,180,156,0) 100%),
      radial-gradient(ellipse 46% 44% at 50% 34%, var(--hair-dark) 0%, rgba(74,58,52,0) 100%),
      radial-gradient(ellipse 70% 34% at 50% 100%, var(--vest) 0%, rgba(232,105,42,0.5) 60%, rgba(232,105,42,0) 100%),
      linear-gradient(160deg, var(--studio-light), #b9b1ad 60%, #a59892);
  }
  .photo-portrait-right {
    left: 557px; top: 368px; width: 643px; height: 687px;
    background:
      radial-gradient(ellipse 26% 24% at 44% 34%, var(--skin) 0%, rgba(226,180,156,0.6) 55%, rgba(226,180,156,0) 100%),
      radial-gradient(ellipse 64% 36% at 55% 100%, var(--jacket) 0%, rgba(43,42,48,0.7) 60%, rgba(43,42,48,0) 100%),
      radial-gradient(ellipse 14% 10% at 44% 66%, #c7303a 0%, rgba(199,48,58,0) 100%),
      linear-gradient(160deg, #b5b1b2, var(--studio-grey) 70%, #6e6a6d);
  }
  .photo-small-1 {
    left: 0; top: 1080px; width: 394px; height: 306px;
    background:
      radial-gradient(ellipse 16% 18% at 40% 30%, var(--skin) 0%, rgba(226,180,156,0) 100%),
      radial-gradient(ellipse 40% 42% at 42% 92%, var(--vest) 0%, rgba(232,105,42,0.6) 55%, rgba(232,105,42,0) 100%),
      linear-gradient(170deg, var(--studio-light), #b4aca8);
  }
  .photo-small-2 {
    left: 410px; top: 1080px; width: 403px; height: 306px;
    background:
      radial-gradient(ellipse 12% 16% at 50% 38%, var(--skin) 0%, rgba(226,180,156,0) 100%),
      radial-gradient(ellipse 38% 34% at 50% 80%, var(--jersey) 0%, rgba(127,168,204,0.6) 55%, rgba(127,168,204,0) 100%),
      linear-gradient(170deg, #d4cdc6, #bcb2a7);
  }
  .photo-small-3 {
    left: 825px; top: 1080px; width: 375px; height: 306px;
    background:
      radial-gradient(ellipse 48% 22% at 55% 62%, rgba(200,90,110,0.75) 0%, rgba(200,90,110,0) 100%),
      linear-gradient(180deg, var(--sky) 0%, #d8e8f2 38%, var(--sea) 46%, var(--grass) 62%, #a9a59c 100%);
  }

  .service { position: absolute; top: 1436px; left: 0; width: 1200px; text-align: center; }
  .service-title {
    display: flex; align-items: center; justify-content: center; gap: 34px;
    font-family: "Bebas Neue", sans-serif; font-weight: 400; color: var(--heading);
    font-size: 122px; line-height: 1; letter-spacing: 1px;
  }
  .service-title::before, .service-title::after {
    content: ""; width: 100px; height: 4px; background: var(--heading);
  }
  .service-text {
    margin: 40px auto 0; width: 1100px;
    font-family: "Mulish", sans-serif; font-weight: 400; color: var(--text);
    font-size: 40px; line-height: 60px;
  }

  .tagline {
    position: absolute; left: 62px; top: 2110px;
    font-family: "Bebas Neue", sans-serif; font-size: 112px; line-height: 95px;
    color: var(--white); list-style: none;
  }
  .tagline .we { color: var(--accent-pink); }
  .contact {
    position: absolute; left: 492px; top: 2342px; list-style: none;
    font-family: "Bebas Neue", sans-serif; font-size: 78px; line-height: 64px; color: var(--white);
  }
  .contact li { display: flex; align-items: center; gap: 22px; }
  .contact svg { width: 34px; height: 34px; flex: none; }
</style>
</head>
<body>
<main class="flyer">
  <svg class="bands" width="1200" height="2520" viewBox="0 0 1200 2520" aria-hidden="true">
    <defs>
      <linearGradient id="band-top" x1="0" y1="0" x2="1" y2="1">
        <stop offset="0" stop-color="#5a1f8f"/>
        <stop offset="1" stop-color="#a82792"/>
      </linearGradient>
      <linearGradient id="band-bottom" x1="0" y1="0" x2="1" y2="0.4">
        <stop offset="0" stop-color="#5a1f8f"/>
        <stop offset="1" stop-color="#c2288e"/>
      </linearGradient>
    </defs>
    <polygon points="0,0 1200,0 1200,315 0,526" fill="url(#band-top)"/>
    <polygon points="0,2048 1200,2173 1200,2520 0,2520" fill="url(#band-bottom)"/>
  </svg>

  <header class="brand">
    <span class="brand-dot" aria-hidden="true"></span>
    <span class="brand-name">Harbor Pathways</span>
  </header>

  <div class="photo photo-portrait-left" role="img" aria-label="Photo of a smiling young woman in a hi-vis vest"></div>
  <div class="photo photo-portrait-right" role="img" aria-label="Photo of a smiling young man in a dark jacket"></div>
  <div class="photo photo-small-1" role="img" aria-label="Photo of a young man in an orange vest"></div>
  <div class="photo photo-small-2" role="img" aria-label="Photo of a man cheering with raised fists"></div>
  <div class="photo photo-small-3" role="img" aria-label="Photo of a group of friends at a picnic table by the beach"></div>

  <section class="service">
    <h1 class="service-title">Children &amp; Families</h1>
    <p class="service-text">Harbor Pathways welcomes children and families.<br>Children are supported to develop friendships,<br>life skills and a sense of community.<br>Our friendly, experienced teams and qualified<br>KITE leaders, provide a dynamic range of<br>play-based activities that reflect your child’s<br>interests, abilities and culture.</p>
  </section>

  <ul class="tagline">
    <li><span class="we">We</span> Listen</li>
    <li><span class="we">We</span> Plan</li>
    <li><span class="we">We</span> Do</li>
    <li><span class="we">We</span> Care</li>
  </ul>

  <ul class="contact">
    <li>
      <svg viewBox="0 0 24 24" aria-hidden="true"><circle cx="12" cy="12" r="10" fill="none" stroke="#fff" stroke-width="2.4"/><path d="M2 12h20M12 2c3 3 3 17 0 20M12 2c-3 3-3 17 0 20" fill="none" stroke="#fff" stroke-width="1.8"/></svg>
      harborpathways.com.au
    </li>
    <li>
      <svg viewBox="0 0 24 24" aria-hidden="true"><path d="M6.6 2.5l3 3.2-1.8 2.6c1.3 2.9 3.5 5.1 6.4 6.4l2.6-1.8 3.2 3-1.6 3.6C10.6 19.7 4.3 13.4 3 5.4z" fill="#fff"/></svg>
      (02) 5550 1900
    </li>
  </ul>
</main>
</body>
</html>
```